Criação de Logo + Papelaria + Manual Básico para Arquitetura
" Somos uma empresa pequena, eu e a minha sócia Clarice, atendemos o cliente, fazemos o levantamento de medidas e necessidades do cliente, desenvolvemos o projeto desde o início em 3D colorido, depois o projeto executivo e acompanhamento de obras. Estamos presentes no processo do início ao fim. Buscamos sempre atender o cliente da melhor maneira possível, sempre estando a par de todo o projeto. "

```html
<!DOCTYPE html>
<html lang="pt-BR">
<head>
<meta charset="UTF-8">
<title>Cartão de visita — Traço Estúdio</title>
<link rel="stylesheet" href="https://fonts.googleapis.com/css2?family=Open+Sans:wght@400;600;700&display=swap">
<style>
  :root {
    --backdrop: #e8e5e1;
    --panel-grey: #8a8b8d;
    --card-white: #ffffff;
    --ink: #5b5c5e;
    --ink-soft: #6f7072;
    --rule: #b9babc;
    --on-grey: #ffffff;
  }
  * { margin: 0; padding: 0; box-sizing: border-box; }
  html, body {
    width: 1200px; height: 1200px; overflow: hidden;
    background: var(--backdrop);
    font-family: "Open Sans", Arial, sans-serif;
  }
  .canvas {
    width: 1200px; height: 1200px;
    display: flex; align-items: center; justify-content: center;
  }
  .business-card {
    width: 900px; height: 290px;
    display: flex;
    background: var(--card-white);
    border-radius: 90px 0 90px 0;
    overflow: hidden;
    box-shadow: 0 6px 18px rgba(0,0,0,0.12);
  }
  .brand-panel {
    width: 432px; height: 100%;
    background: var(--panel-grey);
    display: flex; flex-direction: column;
    align-items: center; justify-content: center;
    color: var(--on-grey);
  }
  .brand-name {
    font-weight: 400;
    font-size: 40px;
    letter-spacing: 6px;
    text-transform: uppercase;
    line-height: 1.2;
    text-align: center;
  }
  .brand-tagline {
    margin-top: 10px;
    font-size: 11px;
    letter-spacing: 3.5px;
    text-transform: uppercase;
    font-weight: 400;
  }
  .contact-panel {
    flex: 1;
    padding: 42px 40px 0 48px;
    color: var(--ink);
  }
  .person-name {
    font-size: 28px; font-weight: 600;
    padding-bottom: 4px;
    border-bottom: 2px solid var(--rule);
    width: 290px;
  }
  .person-role {
    margin-top: 10px;
    font-size: 17px; font-weight: 700;
  }
  .contact-list {
    list-style: none;
    margin-top: 22px;
    padding-left: 40px;
  }
  .contact-item {
    display: flex; align-items: center; gap: 12px;
    font-size: 16px; color: var(--ink-soft);
    height: 36px;
  }
  .contact-icon { width: 20px; height: 20px; fill: var(--ink); flex-shrink: 0; }
</style>
</head>
<body>
<main class="canvas">
  <article class="business-card">
    <section class="brand-panel">
      <div class="brand-name">Traço<br>Estúdio</div>
      <div class="brand-tagline">Arquitetura e interiores</div>
    </section>
    <section class="contact-panel">
      <h1 class="person-name">Renata Clarice</h1>
      <p class="person-role">Cargo Nome</p>
      <ul class="contact-list">
        <li class="contact-item">
          <svg class="contact-icon" viewBox="0 0 24 24" aria-hidden="true"><path d="M6.6 10.8c1.4 2.8 3.8 5.1 6.6 6.6l2.2-2.2c.3-.3.7-.4 1-.2 1.1.4 2.3.6 3.6.6.6 0 1 .4 1 1V20c0 .6-.4 1-1 1C10.6 21 3 13.4 3 4c0-.6.4-1 1-1h3.5c.6 0 1 .4 1 1 0 1.3.2 2.5.6 3.6.1.3 0 .7-.2 1z"/></svg>
          <span>(000) 0000-0000</span>
        </li>
        <li class="contact-item">
          <svg class="contact-icon" viewBox="0 0 24 24" aria-hidden="true"><path d="M3 5h18v14H3z M4.5 6.5v.3L12 12l7.5-5.2v-.3z" fill-rule="evenodd"/></svg>
          <span>xxxxx@xxxxx.com.br</span>
        </li>
        <li class="contact-item">
          <svg class="contact-icon" viewBox="0 0 24 24" aria-hidden="true"><path fill="none" stroke="currentColor" d="" /><circle cx="12" cy="12" r="9" fill="none" stroke="#5b5c5e" stroke-width="1.6"/><ellipse cx="12" cy="12" rx="4" ry="9" fill="none" stroke="#5b5c5e" stroke-width="1.4"/><path d="M3 12h18" stroke="#5b5c5e" stroke-width="1.4"/></svg>
          <span>www.xxxxxxxxxx.com.br</span>
        </li>
      </ul>
    </section>
  </article>
</main>
</body>
</html>
```